TBW Construction
Stationary and Business Cards
Professional
Darek Venhollis
President
518 Marlow Ave
Harwick, PA 18321
office@tbwbuilders-example.net
tbwconstruction-example.com
NJ Lic# 58KT31720485
Commercial, Residential & Industrial

```html
<!DOCTYPE html>
<html lang="en">
<head>
<meta charset="utf-8">
<title>TBW Construction — Business Cards</title>
<link href="https://fonts.googleapis.com/css2?family=Michroma&family=Montserrat:wght@500;700&display=swap" rel="stylesheet">
<style>
  :root {
    --bg: #e6e7e9;
    --card: #ffffff;
    --navy: #1f4a7c;
    --steel: #7d8894;
    --ink: #4a5560;
    --band-light: #dfe4ea;
  }
  * { margin: 0; padding: 0; box-sizing: border-box; }
  html, body { width: 1200px; height: 988px; overflow: hidden; background: var(--bg); }
  .sheet { position: relative; width: 1200px; height: 988px; }
  .card {
    position: absolute; left: 220px; width: 760px; height: 434px;
    background: var(--card);
    box-shadow: 0 6px 18px rgba(0,0,0,.18);
    overflow: hidden;
  }
  .card--back { top: 40px; }
  .card--front { top: 514px; }

  .brand { position: absolute; left: 0; right: 0; text-align: center; white-space: nowrap; }
  .brand-mark { display: inline-block; background: var(--navy); vertical-align: middle; }
  .brand-name {
    font-family: "Montserrat", sans-serif; font-weight: 700;
    color: var(--navy); letter-spacing: 2px; vertical-align: middle;
  }
  .web-line {
    font-family: "Michroma", sans-serif; font-size: 10px; letter-spacing: 4px;
    text-transform: lowercase; white-space: nowrap;
  }

  .card--back .brand { top: 160px; }
  .card--back .brand-mark { width: 24px; height: 24px; margin-right: 14px; }
  .card--back .brand-name { font-size: 40px; }
  .card--back .web-line {
    position: absolute; top: 300px; left: 0; right: 0; text-align: center; color: var(--steel);
  }

  .card--front .brand { top: 48px; }
  .card--front .brand-mark { width: 22px; height: 22px; margin-right: 12px; }
  .card--front .brand-name { font-size: 38px; }

  .person {
    position: absolute; top: 140px; right: 400px; text-align: right;
    font-family: "Montserrat", sans-serif; color: var(--ink);
  }
  .person-name { font-family: "Michroma", sans-serif; font-size: 12px; color: var(--navy); letter-spacing: 1.5px; }
  .person-title { font-size: 10px; letter-spacing: 2px; text-transform: uppercase; margin-top: 4px; color: var(--steel); }
  .person-address { margin-top: 8px; font-size: 11px; line-height: 17px; letter-spacing: 1px; }

  .contacts {
    position: absolute; top: 134px; left: 385px; list-style: none;
    font-family: "Montserrat", sans-serif; font-size: 11px; color: var(--ink); letter-spacing: .5px;
  }
  .contacts li { display: flex; align-items: center; height: 22px; }
  .contacts svg { width: 15px; height: 15px; margin-right: 8px; flex: none; }

  .band-stripe { position: absolute; left: 0; right: 0; height: 4px; background: var(--band-light); }
  .band-stripe--top { top: 252px; }
  .band { position: absolute; left: 0; right: 0; top: 262px; height: 46px; background: var(--navy); }
  .band-stripe--bottom { top: 314px; }
  .band-foot { position: absolute; left: 0; right: 0; top: 332px; height: 4px; background: var(--navy); }
  .card--front .web-line {
    position: absolute; top: 354px; left: 70px; color: var(--navy);
  }
</style>
</head>
<body>
<main class="sheet">
  <section class="card card--back" aria-label="Business card back">
    <div class="brand"><span class="brand-mark"></span><span class="brand-name">TBW Construction</span></div>
    <p class="web-line">www.tbwconstruction-example.com</p>
  </section>

  <section class="card card--front" aria-label="Business card front">
    <div class="brand"><span class="brand-mark"></span><span class="brand-name">TBW Construction</span></div>

    <div class="person">
      <p class="person-name">Darek Venhollis</p>
      <p class="person-title">President</p>
      <p class="person-address">518 Marlow Ave<br>Harwick, PA 18321</p>
    </div>

    <ul class="contacts">
      <li><svg viewBox="0 0 18 18"><circle cx="9" cy="9" r="9" fill="#1f4a7c"/><path d="M6 4.5l2 .2.6 2.2-1.2.9a6 6 0 0 0 2.8 2.8l.9-1.2 2.2.6.2 2a1.5 1.5 0 0 1-1.6 1.4A8 8 0 0 1 4.6 6.1 1.5 1.5 0 0 1 6 4.5z" fill="#fff"/></svg>973-555-0142</li>
      <li><svg viewBox="0 0 18 18"><circle cx="9" cy="9" r="9" fill="#1f4a7c"/><rect x="6" y="4" width="6" height="10" rx="1" fill="#fff"/><rect x="7" y="5.5" width="4" height="6" fill="#1f4a7c"/></svg>973-555-0187</li>
      <li><svg viewBox="0 0 18 18"><circle cx="9" cy="9" r="9" fill="#1f4a7c"/><rect x="4.5" y="6" width="9" height="6.5" fill="#fff"/><path d="M4.5 6L9 9.6 13.5 6" stroke="#1f4a7c" stroke-width="1" fill="none"/></svg>office@tbwbuilders-example.net</li>
      <li><svg viewBox="0 0 18 18"><circle cx="9" cy="9" r="9" fill="#1f4a7c"/><circle cx="9" cy="9" r="4.5" stroke="#fff" fill="none"/><path d="M4.5 9h9M9 4.5c-2 2.5-2 6.5 0 9M9 4.5c2 2.5 2 6.5 0 9" stroke="#fff" stroke-width=".8" fill="none"/></svg>www.tbwconstruction-example.com</li>
    </ul>

    <div class="band-stripe band-stripe--top"></div>
    <div class="band"></div>
    <div class="band-stripe band-stripe--bottom"></div>
    <div class="band-foot"></div>
    <p class="web-line">www.tbwconstruction-example.com</p>
  </section>
</main>
</body>
</html>
```